Fine Art business needs new website

We need a simple website with a home page, about us page, New sculptures, Sold sculptures, and a contact us page.Our sculptures are very high end one of a kind pieces. As such we need the site to be VERY elegant and professional. Lastly, because I'll be updating pictures on the website on a monthly basis it needs to be user friendly to update (Wordpress is preferred). The only branding we have so far for the business is a business card.
Updates
I wasn't completely ready when this project launched, also I am on the road right now and haven't been able to be as responsive to all you designers as I would like. I will work on giving feedback to all the top designs we've received so far. Thank you all so much for your participation and hardwork.
Target Market(s)
High end customers (affluent), art collectors, interior decorators/designers
Industry/Entity Type
Art Gallery
Coding
Coded - Design and coding required
Number of Pages Required
5+ page
Requirements
Must have
- Easily editable picture gallery for myself so that I can add new pieces(pictures of the pieces), remove sold pieces, etc. I would like the website to be built in wordpress so I can update it. I currently use larkpanelpro through Hostlark for my other business website and would like to do the same for this one.
- Pages:
- -Intro page with featured pieces
- -Current pieces gallery (for sale) mainly a picture gallery
- -Sculptures archive (sold pieces) another picture gallery
- -About us: Pull-down of -about the artist (attached content)
- -Artistic Process (attached content)
- -Show Schedule:
- -one page dedicated to "friends of VMC" (basically a link page)
- TO BE CLEAR "www.pebblecrew.example" IS A TOTALLY DIFFERENT SITE AND I'M NOT TRYING TO COMBINE THE TWO OR JOIN THEM INTO ONE. This page needs be more elegant and seperate from the Pebble Crew site.
- UPDATE: I'd like a link to the VMC Chatterloop page: https://www.chatterloop.example/velmormillco/
Nice to have
- I would like the pictures on the gallery pages able to have text connected with them (Materials, price)
- I would like the site style and fonts to be similar to our business cards we've already had designed (picture attached).
Should not have
- Too much flash or other things that will make the site slow to load.

```html
<!DOCTYPE html>
<html lang="en">
<head>
<meta charset="utf-8">
<title>Velmor Mill Co — Schedule</title>
<link rel="stylesheet" href="https://fonts.googleapis.com/css2?family=Cinzel:wght@600;700&family=Yesteryear&family=Cardo:wght@400;700&family=Arimo&display=swap">
<style>
:root{
  --bg:#efeeef;
  --plum:#3f2866;
  --plum-soft:#8f7fae;
  --plum-mist:#d7d0e2;
  --text:#3e3434;
  --line:#c9c5cc;
  --photo-dark:#2a1d38;
  --photo-deep:#1a1224;
}
*{box-sizing:border-box;margin:0;padding:0}
html,body{width:1200px;height:1099px;overflow:hidden}
body{background:var(--bg);position:relative;font-family:"Cardo",serif;color:var(--text)}
.abs{position:absolute}

.brand{left:197px;top:14px;width:170px;height:76px;display:flex;align-items:center;gap:9px}
.brand-dot{width:22px;height:22px;border-radius:50%;background:var(--plum)}
.brand-name{font-size:17px;color:var(--plum);letter-spacing:.5px}

.contact{left:844px;top:22px;font-family:"Arimo",sans-serif;font-size:10.5px;color:#555;line-height:1.05}
.contact-row{display:flex;gap:5px;align-items:flex-start;margin-bottom:7px}
.contact-row svg{flex:none;margin-top:1px}

.nav{left:193px;top:108px;width:814px;height:34px;border-top:1px solid var(--line);border-bottom:1px solid var(--line);display:flex;justify-content:space-between;padding:0 14px}
.nav a{font-family:"Cinzel",serif;font-weight:700;font-size:16.5px;color:var(--plum);text-decoration:none;line-height:32px;letter-spacing:.3px}
.nav a.current{border-bottom:3px solid var(--plum)}

.section-head{left:193px;width:814px;height:34px;border-bottom:1px solid var(--line)}
.section-title{position:absolute;left:32px;top:2px;display:flex;align-items:center;gap:10px;font-family:"Yesteryear",cursive;font-size:26px;color:var(--plum)}
.pager{position:absolute;right:10px;top:10px;font-size:10.5px;font-weight:700;color:#4a4050;display:flex;gap:8px;align-items:center}
.pager .on{text-decoration:underline;color:var(--plum)}

.geode{z-index:0;box-shadow:6px 8px 14px rgba(80,60,90,.18)}
.geode-amethyst{border-radius:46% 54% 42% 58%/55% 45% 55% 45%;
  background:radial-gradient(ellipse 48% 44% at 52% 50%,#6f5a8c 0%,#8a78a6 45%,#b2a5c2 68%,#d6cfdc 82%,#cfc7d4 100%);opacity:.85}
.geode-agate{border-radius:40% 60% 55% 45%/48% 42% 58% 52%;
  background:radial-gradient(ellipse 42% 44% at 50% 52%,#e9e9f1 0%,#d8d8e6 50%,#c2b4cc 66%,#b58fa4 74%,#e6dfe4 84%,#d4ccd2 100%);opacity:.9}
.geode-cream{border-radius:50% 42% 48% 55%/46% 52% 48% 54%;
  background:radial-gradient(ellipse 45% 45% at 55% 50%,#f4efe6 0%,#e8dccd 55%,#d7c7b6 80%,#e9e2d8 100%);opacity:.9}

.card{z-index:1;width:166px;height:228px;border:2px solid var(--plum);border-top:1px solid var(--plum-mist);background:rgba(242,240,243,.45);box-shadow:0 0 14px rgba(120,100,140,.18) inset;text-align:center}
.card-photo{position:absolute;left:22px;top:14px;width:120px;height:151px;background-color:var(--photo-deep)}
.photo-malachite{background:radial-gradient(ellipse 30% 42% at 50% 42%,#2f8a6a,#1c4d40 55%,transparent 80%),linear-gradient(var(--photo-dark),var(--photo-deep))}
.photo-amethyst{background:radial-gradient(ellipse 32% 44% at 50% 42%,#6a4fb0,#3b2a6e 55%,transparent 80%),linear-gradient(var(--photo-dark),var(--photo-deep))}
.photo-ammonite{background:radial-gradient(ellipse 44% 30% at 50% 48%,#b08a55,#6e5234 55%,transparent 80%),linear-gradient(var(--photo-dark),var(--photo-deep))}
.photo-geode{background:radial-gradient(ellipse 14% 22% at 52% 40%,#c9b57a,transparent 70%),radial-gradient(ellipse 36% 44% at 48% 40%,#4a2f8c,#2d1f5a 60%,transparent 82%),linear-gradient(var(--photo-dark),var(--photo-deep))}
.photo-amber{background:radial-gradient(ellipse 28% 44% at 50% 45%,#d4932e,#8a521c 55%,transparent 80%),linear-gradient(var(--photo-dark),var(--photo-deep))}
.photo-agate{background:radial-gradient(ellipse 22% 44% at 50% 44%,#d9dde4,#7f90a8 55%,transparent 80%),linear-gradient(var(--photo-dark),var(--photo-deep))}
.photo-bronze{background:radial-gradient(ellipse 34% 40% at 52% 50%,#c88a3e,#7a4e22 55%,transparent 80%),linear-gradient(var(--photo-dark),var(--photo-deep))}
.photo-coral{background:radial-gradient(ellipse 28% 44% at 50% 44%,#d9c49a,#8c7550 55%,transparent 80%),linear-gradient(var(--photo-dark),var(--photo-deep))}

.card-name{position:absolute;left:0;right:0;top:170px;font-family:"Yesteryear",cursive;font-size:13px;color:var(--plum)}
.card-name span{border-bottom:1px solid var(--plum)}
.card-meta{position:absolute;left:0;right:0;top:190px;font-size:11.5px;line-height:15.5px;color:var(--text)}

.badge{position:absolute;left:0;top:32px;width:166px;height:50px}
.badge-band{position:absolute;left:26px;right:0;top:19px;height:16px;background:linear-gradient(90deg,rgba(90,60,120,.6),rgba(200,190,215,.75));border-top:1px solid rgba(255,255,255,.6)}
.badge-ring{position:absolute;left:1px;top:0;width:50px;height:50px;border-radius:50%;border:2px solid var(--plum-soft);background:rgba(90,60,120,.4)}
.badge-label{position:absolute;left:6px;top:10px;font-size:18px;color:#fff}

.divider{left:0;top:710px;width:1200px;height:1px;background:var(--line)}

.footer{z-index:2;left:193px;top:1026px;width:814px;height:53px;border-top:1px solid var(--line);border-bottom:1px solid var(--line)}
.follow{position:absolute;left:57px;top:14px;display:flex;align-items:center;gap:4px;font-family:"Yesteryear",cursive;font-size:18px;color:var(--plum)}
.social{width:20px;height:20px;border-radius:50%;border:1.5px solid var(--plum-soft);background:#ece8f0;display:flex;align-items:center;justify-content:center}
.signup{position:absolute;left:368px;top:12px;font-family:"Yesteryear",cursive;font-size:22px;color:var(--plum);white-space:nowrap}
.newsletter{position:absolute;left:597px;top:12px;width:190px;height:30px;display:flex;border:1px solid #b9b1c6}
.newsletter-field{flex:1;background:#f7f6f8;font-size:12.5px;color:#777;line-height:28px;padding-left:17px}
.newsletter-btn{width:61px;background:linear-gradient(#6d5891,#4c3570);color:#fff;font-size:13px;line-height:28px;text-align:center}
.copyright{left:219px;top:1083px;font-family:"Arimo",sans-serif;font-size:9px;color:#666}
</style>
</head>
<body>

<div class="abs brand"><span class="brand-dot"></span><span class="brand-name">Velmor Mill Co</span></div>

<div class="abs contact">
  <div class="contact-row"><svg width="10" height="14" viewBox="0 0 10 14"><path d="M5 1a4 4 0 0 1 4 4c0 3-4 8-4 8S1 8 1 5a4 4 0 0 1 4-4z" fill="none" stroke="#555"/><circle cx="5" cy="5" r="1.5" fill="#555"/></svg><span>PO box 400218<br>Larkfield Bend CO 80999</span></div>
  <div class="contact-row"><span style="width:10px">@</span><span>ari@thepebblecrew.example</span></div>
  <div class="contact-row"><svg width="10" height="10" viewBox="0 0 10 10"><path d="M2 1l2 2-1 1.5c.6 1.2 1.3 1.9 2.5 2.5L7 6l2 2-1.5 1.5C4 9 1 6 .5 2.5z" fill="none" stroke="#555"/></svg><span>+1.5550142286</span></div>
</div>

<nav class="abs nav">
  <a href="#">HOME</a><a href="#">ABOUT US</a><a href="#" class="current">SCHEDULE</a><a href="#">ARTISTIC PROCESS</a><a href="#">CONTACT US</a><a href="#">EVENTS</a>
</nav>

<div class="abs section-head" style="top:148px">
  <div class="section-title"><svg width="36" height="18" viewBox="0 0 36 18"><path d="M0 0h8l9 9-9 9H0l9-9z" fill="#7c62a4"/><path d="M16 0h8l9 9-9 9h-8l9-9z" fill="#5a3f86"/></svg>New Schedule</div>
  <div class="pager"><span>‹ Prev</span><span>1</span><span class="on">2</span><span>3</span><span>Next ›</span></div>
</div>

<div class="abs geode geode-amethyst" role="img" aria-label="Amethyst geode slice" style="left:90px;top:227px;width:138px;height:170px"></div>
<div class="abs geode geode-agate" role="img" aria-label="White agate geode half" style="left:764px;top:266px;width:94px;height:158px"></div>
<div class="abs geode geode-cream" role="img" aria-label="Cream agate geode half" style="left:150px;top:540px;width:100px;height:133px"></div>
<div class="abs geode geode-amethyst" role="img" aria-label="Amethyst geode slice" style="left:934px;top:531px;width:130px;height:146px"></div>
<div class="abs geode geode-agate" role="img" aria-label="White agate geode half" style="left:951px;top:900px;width:130px;height:150px"></div>

<div class="abs divider"></div>

<div class="abs section-head" style="top:720px">
  <div class="section-title"><svg width="36" height="18" viewBox="0 0 36 18"><path d="M0 0h8l9 9-9 9H0l9-9z" fill="#7c62a4"/><path d="M16 0h8l9 9-9 9h-8l9-9z" fill="#5a3f86"/></svg>Most Popular</div>
  <div class="pager"><span>‹ Prev</span><span>1</span><span class="on">2</span><span>3</span><span>Next ›</span></div>
</div>

<div class="abs card" style="left:200px;top:200px"><div class="card-photo photo-malachite" role="img" aria-label="Green malachite sculpture on a stand"></div><div class="badge"><div class="badge-band"></div><div class="badge-ring"></div><div class="badge-label">New</div></div><div class="card-name"><span>Name of The Schedule</span></div><div class="card-meta">Material<br>Price 123 $</div></div>
<div class="abs card" style="left:411px;top:200px"><div class="card-photo photo-amethyst" role="img" aria-label="Amethyst cluster sculpture on a stand"></div><div class="card-name"><span>Name of The Schedule</span></div><div class="card-meta">Material<br>Price 123 $</div></div>
<div class="abs card" style="left:623px;top:200px"><div class="card-photo photo-ammonite" role="img" aria-label="Ammonite and horn sculpture on a stand"></div><div class="card-name"><span>Name of The Schedule</span></div><div class="card-meta">Material<br>Price 123 $</div></div>
<div class="abs card" style="left:835px;top:200px"><div class="card-photo photo-geode" role="img" aria-label="Amethyst geode sculpture with gold stand"></div><div class="badge"><div class="badge-band"></div><div class="badge-ring"></div><div class="badge-label">Sale</div></div><div class="card-name"><span>Name of The Schedule</span></div><div class="card-meta">Material<br>Price 123 $</div></div>

<div class="abs card" style="left:198px;top:456px"><div class="card-photo photo-ammonite" role="img" aria-label="Ammonite and horn sculpture on a stand"></div><div class="card-name"><span>Name of The Schedule</span></div><div class="card-meta">Material<br>Price 123 $</div></div>
<div class="abs card" style="left:411px;top:456px"><div class="card-photo photo-geode" role="img" aria-label="Amethyst geode sculpture with gold stand"></div><div class="card-name"><span>Name of The Schedule</span></div><div class="card-meta">Material<br>Price 123 $</div></div>
<div class="abs card" style="left:623px;top:456px"><div class="card-photo photo-amethyst" role="img" aria-label="Amethyst cluster sculpture on a stand"></div><div class="badge" style="top:0"><div class="badge-band"></div><div class="badge-ring"></div><div class="badge-label">New</div></div><div class="card-name"><span>Name of The Schedule</span></div><div class="card-meta">Material<br>Price 123 $</div></div>
<div class="abs card" style="left:835px;top:456px"><div class="card-photo photo-malachite" role="img" aria-label="Green malachite sculpture on a stand"></div><div class="card-name"><span>Name of The Schedule</span></div><div class="card-meta">Material<br>Price 123 $</div></div>

<div class="abs card" style="left:197px;top:772px"><div class="card-photo photo-amber" role="img" aria-label="Amber ammonite sculpture on a stand"></div><div class="badge"><div class="badge-band"></div><div class="badge-ring"></div><div class="badge-label">Sold</div></div><div class="card-name"><span>Name of The Schedule</span></div><div class="card-meta">Material<br>Price 123 $</div></div>
<div class="abs card" style="left:409px;top:772px"><div class="card-photo photo-agate" role="img" aria-label="Blue agate slice sculpture on a stand"></div><div class="card-name"><span>Name of The Schedule</span></div><div class="card-meta">Material<br>Price 123 $</div></div>
<div class="abs card" style="left:620px;top:772px"><div class="card-photo photo-bronze" role="img" aria-label="Bronze spiral shell sculpture"></div><div class="card-name"><span>Name of The Schedule</span></div><div class="card-meta">Material<br>Price 123 $</div></div>
<div class="abs card" style="left:832px;top:772px"><div class="card-photo photo-coral" role="img" aria-label="Golden coral stone sculpture on a stand"></div><div class="badge"><div class="badge-band"></div><div class="badge-ring"></div><div class="badge-label">Sold</div></div><div class="card-name"><span>Name of The Schedule</span></div><div class="card-meta">Material<br>Price 123 $</div></div>

<footer class="abs footer">
  <div class="follow">Follow Us:
    <span class="social" aria-label="Chatterloop"></span>
    <span class="social" aria-label="Photo feed"></span>
    <span class="social" aria-label="Social network"></span>
    <span class="social" aria-label="Email"><svg width="11" height="8" viewBox="0 0 11 8"><rect x=".5" y=".5" width="10" height="7" fill="none" stroke="#6a5890"/><path d="M.5.5l5 4 5-4" fill="none" stroke="#6a5890"/></svg></span>
  </div>
  <div class="signup">Sign Up For Our Newsletter</div>
  <div class="newsletter"><div class="newsletter-field">Your email address</div><div class="newsletter-btn">SUBMIT</div></div>
</footer>

<div class="abs copyright">Velmor Mill Co © 2018 All rights reserved</div>

</body>
</html>
```